NOTE: I PROVIDED THE INCORRECT LOGO AND ONLY A HANDFUL OF PEOPLE NOTICED THAT IT WAS NOT THE ONE I DESCRIBED. THE LOGO I HAVE NOW ATTACHED MATCHES MY WEBSITE AND THE COLORS ON THE WEBSITE SHOULD BE USED FOR THE CARD.

PLEASE READ THE BUSINESS CARD DETAILS AND PROJECT MUST HAVES CAREFULLY.

I am looking for a business card that is powerful, a bit edgy, and although I work in the corporate world, not too formal. I would like to see designs that use the colors on my website www.brightmoorlane.com. I don't want the card to look washed out so please use shades of those colors that make them "pop". The "vibe" of the card needs to show substance and confidence while also reflecting that we're not your usual consultants.

The focus of my work is turning "people problems" into profits. Those problems could be poor service, an unstable workforce, untrained leaders, or managing change. We are an aggressive, results-focused team of performance improvement professionals who refuse to believe "things can't be done". For us, failure is not an option. Our logo reflects a target from the view of the site on a gun.

In addition to the contact information provided on the sample business card (do not include "turning people problems into profits"), I would like to include this statement (probably on the back):
I equip results-oriented business leaders to turn their people problems into profits in six months or less.

PLEASE NOTE THAT MY WEBSITE IS UNDER REVISION TO TONE DOWN THE MILITARY THEME, ALTHOUGH THE WARRIOR ENERGY AND FOCUS ON RESULTS REMAINS.

Target Market(s)

My clients are Mid and senior-level managers. I don't target any particular industry.

Industry/Entity Type

Consulting

Contact Information for Business Card

In addition to the contact information provided on the sample business card (DO NOT INCLUDE "turning people problems into profits"), I would like to include this statement (probably on the back):

I don't care whether the card is landscape or portrait view.

Font styles to use
Sans Serif

Requirements
Must have
• 1. be easy to read, no 6-8 point fonts!
• 2. a "vibe" that captures the eye without being too chaotic or busy
• 3. bold color, not washed out or boring - a good blend with the colors currently on my website (black, red, white, army green) but you don't need to use all of them.
• 4. all the contact information I have provided
• 5. a good blend with the colors currently on my website
• 6. Must have this quote on the back of the card: I equip results-oriented business leaders to turn their people problems into profits in six months or less.
Nice to have
• In looking at the sample images I provided for ideas, you can see that I like the way a card carries over from one side to the next.
• It would be great to find some aspect/quality/feature that I haven't seen before
Should not have
• 1. NO use of ALL CAPS
• 2. fonts that I would have to seek out and purchase (you should provide files for font if using something not standard)

```html
<!DOCTYPE html>
<html lang="en">
<head>
<meta charset="utf-8">
<title>Brightmoor Lane – Business Card</title>
<link rel="stylesheet" href="https://fonts.googleapis.com/css2?family=Rubik:wght@400;500;700&display=swap">
<style>
  :root {
    --olive: #3a3d2f;
    --red: #ea3a30;
    --red-soft: #f0544a;
    --white: #ffffff;
    --ink: #2e302a;
    --stage: #2a2c31;
  }
  * { box-sizing: border-box; margin: 0; padding: 0; }
  html, body { width: 1200px; height: 900px; overflow: hidden; }
  body {
    background: var(--stage);
    font-family: "Rubik", Arial, sans-serif;
    position: relative;
  }
  .card {
    position: absolute;
    width: 540px;
    height: 310px;
    border-radius: 24px;
    overflow: hidden;
    box-shadow: 0 18px 40px rgba(0,0,0,.45);
  }
  .card svg.card-art { position: absolute; inset: 0; width: 100%; height: 100%; }

  /* Back */
  .card-back { left: 60px; top: 470px; background: var(--red); }
  .back-brand {
    position: absolute; left: 0; right: 0; top: 103px;
    display: flex; align-items: center; justify-content: center; gap: 12px;
    color: var(--white); font-weight: 700; font-size: 32px;
  }
  .brand-dot {
    width: 26px; height: 26px; border-radius: 50%; background: var(--white); flex: none;
  }
  .back-statement {
    position: absolute; left: 70px; right: 70px; top: 214px;
    color: var(--white); font-size: 18px; line-height: 1.3; text-align: center;
  }

  /* Front */
  .card-front { left: 600px; top: 130px; background: var(--white); }
  .holder { position: absolute; left: 34px; top: 34px; }
  .holder-name { color: var(--red); font-weight: 700; font-size: 27px; }
  .holder-title { color: var(--ink); font-size: 16px; margin-top: 2px; }
  .contact-list { list-style: none; position: absolute; left: 34px; top: 112px; }
  .contact-list li {
    display: flex; align-items: center; gap: 10px;
    color: var(--ink); font-size: 16px; margin-bottom: 9px;
  }
  .contact-icon {
    width: 22px; height: 22px; border-radius: 50%; background: var(--olive);
    display: flex; align-items: center; justify-content: center; flex: none;
  }
  .contact-icon svg { width: 12px; height: 12px; }
  .email-domain { color: var(--red); }
  .front-brand {
    position: absolute; right: 30px; top: 122px;
    display: flex; align-items: center; gap: 10px;
    color: var(--olive); font-weight: 700; font-size: 28px;
  }
  .front-brand .brand-dot { background: var(--olive); }
  .front-web {
    position: absolute; right: 34px; bottom: 26px;
    color: var(--white); font-weight: 500; font-size: 18px;
  }
</style>
</head>
<body>

  <section class="card card-back" aria-label="Card back">
    <svg class="card-art" viewBox="0 0 540 310" aria-hidden="true">
      <rect x="0" y="0" width="540" height="125" fill="var(--olive)"/>
      <line x1="0" y1="125" x2="110" y2="125" stroke="var(--white)" stroke-width="3"/>
      <line x1="430" y1="125" x2="540" y2="125" stroke="var(--white)" stroke-width="3"/>
      <line x1="270" y1="28" x2="270" y2="65" stroke="var(--white)" stroke-width="3"/>
      <line x1="270" y1="185" x2="270" y2="204" stroke="var(--white)" stroke-width="3"/>
      <rect x="110" y="65" width="320" height="120" rx="60" fill="var(--olive)" stroke="var(--white)" stroke-width="3"/>
    </svg>
    <div class="back-brand"><span class="brand-dot"></span>Brightmoor Lane</div>
    <p class="back-statement">I equip results-oriented business leaders to turn their people problems into profits in six months or less</p>
  </section>

  <section class="card card-front" aria-label="Card front">
    <svg class="card-art" viewBox="0 0 540 310" aria-hidden="true">
      <path d="M300 0 H540 V92 C480 66 420 56 360 38 C330 28 312 14 300 0 Z" fill="var(--olive)"/>
      <path d="M240 310 C262 262 300 236 360 232 H540 V310 Z" fill="var(--red)"/>
    </svg>
    <div class="holder">
      <h1 class="holder-name">Dana Whitfield</h1>
      <p class="holder-title">Chief Performance Strategist</p>
    </div>
    <ul class="contact-list">
      <li>
        <span class="contact-icon"><svg viewBox="0 0 12 12"><path d="M2.5 1 L4.5 1 L5 3.5 L3.8 4.4 C4.4 5.8 5.6 7 7 7.6 L7.9 6.4 L10.5 7 V9 C10.5 9.8 9.8 10.5 9 10.5 C4.9 10.4 1.5 7 1 3 C1 1.8 1.6 1 2.5 1 Z" fill="var(--white)"/></svg></span>
        555-014-2281
      </li>
      <li>
        <span class="contact-icon"><svg viewBox="0 0 12 12"><rect x="3" y="0.5" width="6" height="11" rx="1.2" fill="var(--white)"/><rect x="4" y="2" width="4" height="6.5" fill="var(--olive)"/></svg></span>
        555-019-4470
      </li>
      <li>
        <span class="contact-icon"><svg viewBox="0 0 12 12"><rect x="1" y="2.5" width="10" height="7" rx="1" fill="var(--white)"/><path d="M1.5 3 L6 6.5 L10.5 3" fill="none" stroke="var(--olive)" stroke-width="1"/></svg></span>
        <span>danaw@<span class="email-domain">brightmoorlane</span>.com</span>
      </li>
    </ul>
    <div class="front-brand"><span class="brand-dot"></span>Brightmoor Lane</div>
    <p class="front-web">www.brightmoorlane.com</p>
  </section>

</body>
</html>
```